Business Card Design

I am a criminologist running a research and consultancy business on my own (PKConsultants)
I specialise in looking at fraud and other white-collar crimes. Also governance issues..
I would like a professional business card that would be appropriate both in the academic and business sector as I straddle both sectors. Normal shape - not square.
I am interested in seeing border Word Cloud type projects - black on white or white on black..
Example key words would be fraud, research, qualitative, interviews, quantitative, white-collar, reports, government, surveys, sample, governance, assurance, crime, offenders, prison etc (I can provide a full list if this is the option I go for). I also like Word Cloud borders as attached.
I am also interested in seeing other style business cards. Preferably one colour, plus black and white.
In particular I like black backgrounds with coloured words etc - colours like lime green are good.
I also like blues - especially teal if a traditional white background is chosen.
I don't have a logo - unless anyone can think of anything that's particularly appropriate.
Graphics can be used but they would be simple and stylish (dots, squares, lines, curves etc)
I would like the design to translate simply for a header for a website or blog.
My current website is www.pelling-hurst.com but is out of date in terms of what I do and design.
I have attached a number of things that have caught my eye and inspired me.
I have asked for a one-sided business card in the first instance - however if someone comes up with a good cloud design that might go on one side, I would consider a two-sided one.
Design can be landscape or portrait.
Kind Regards
Meg
Landscape
Contact Information for Business Card
PKConsultants
Dr Margery Pelling-Hurst, MSc, BSc, **
42 Brindle Wold
Hadley Cross, Wendshire
KX27 4QD
+44(0)1620 482917
+44(0)7531 804152
www.pelling-hurst.com
margery@pelling-hurst.com

```html
<!DOCTYPE html>
<html lang="en">
<head>
<meta charset="utf-8">
<title>PKConsultants – Business Card</title>
<link rel="stylesheet" href="https://fonts.googleapis.com/css2?family=Oswald:wght@600&family=Poppins:wght@300;500&display=swap">
<style>
  :root {
    --page-bg: #2b2b2b;
    --card-black: #0b0b0b;
    --lime: #4cb848;
    --white: #ffffff;
  }
  html, body {
    margin: 0;
    width: 1200px;
    height: 800px;
    overflow: hidden;
    background: var(--page-bg);
  }
  .card {
    position: absolute;
    left: 100px;
    top: 110px;
    width: 1000px;
    height: 580px;
    background: var(--card-black);
    overflow: hidden;
    font-family: "Poppins", sans-serif;
    color: var(--white);
  }
  .brand {
    position: absolute;
    left: 60px;
    top: 222px;
    width: 370px;
    font-family: "Poppins", sans-serif;
    font-weight: 500;
    font-size: 46px;
    letter-spacing: 0.5px;
    color: var(--lime);
  }
  .divider {
    position: absolute;
    left: 450px;
    top: 130px;
    width: 2px;
    height: 300px;
    background: var(--lime);
  }
  .identity {
    position: absolute;
    right: 70px;
    top: 58px;
    text-align: right;
  }
  .identity .name {
    font-family: "Oswald", sans-serif;
    font-weight: 600;
    font-size: 34px;
    text-transform: uppercase;
    letter-spacing: 0.5px;
    color: var(--lime);
    line-height: 1.1;
  }
  .identity .credentials {
    font-weight: 300;
    font-size: 22px;
    margin-top: 2px;
  }
  .contact-group {
    position: absolute;
    right: 70px;
    text-align: right;
  }
  .contact-group.phones { top: 200px; }
  .contact-group.online { top: 300px; }
  .contact-group .line {
    font-weight: 300;
    font-size: 22px;
    line-height: 38px;
    padding-right: 50px;
    white-space: nowrap;
  }
  .contact-group .rule {
    height: 2px;
    background: var(--lime);
    margin-right: 46px;
  }
  .contact-group .icon {
    position: absolute;
    right: 0;
    top: 18px;
    width: 40px;
    height: 40px;
  }
  .address-band {
    position: absolute;
    left: 0;
    bottom: 0;
    width: 100%;
    height: 92px;
    background: var(--lime);
    display: flex;
    align-items: center;
    padding-left: 110px;
    box-sizing: border-box;
    font-weight: 300;
    font-size: 24px;
    letter-spacing: 1.5px;
    color: var(--white);
    white-space: nowrap;
  }
  .address-band svg { width: 22px; height: 30px; margin-right: 24px; flex: none; }
</style>
</head>
<body>
  <div class="card">
    <div class="brand">PKConsultants</div>
    <div class="divider"></div>

    <div class="identity">
      <div class="name">Dr Margery Pelling-Hurst</div>
      <div class="credentials">MSc, BSc</div>
    </div>

    <div class="contact-group phones">
      <div class="line">+44(0)1620 482917</div>
      <div class="rule"></div>
      <div class="line">+44(0)7531 804152</div>
      <svg class="icon" viewBox="0 0 40 40" aria-hidden="true">
        <polygon points="20,2 36,11 36,29 20,38 4,29 4,11" fill="var(--lime)"/>
        <path d="M14 12 l4 0 l2 5 l-3 2 a10 10 0 0 0 5 5 l2-3 l5 2 l0 4 a2 2 0 0 1-2 2 a16 16 0 0 1-15-15 a2 2 0 0 1 2-2z" fill="#fff"/>
      </svg>
    </div>

    <div class="contact-group online">
      <div class="line">margery@pelling-hurst.com</div>
      <div class="rule"></div>
      <div class="line">www.pelling-hurst.com</div>
      <svg class="icon" viewBox="0 0 40 40" aria-hidden="true">
        <polygon points="20,2 36,11 36,29 20,38 4,29 4,11" fill="var(--lime)"/>
        <rect x="11" y="12" width="18" height="12" rx="1" fill="none" stroke="#fff" stroke-width="2"/>
        <rect x="15" y="27" width="10" height="2" fill="#fff"/>
      </svg>
    </div>

    <div class="address-band">
      <svg viewBox="0 0 22 30" aria-hidden="true">
        <path d="M11 0 a11 11 0 0 1 11 11 c0 8-11 19-11 19 s-11-11-11-19 a11 11 0 0 1 11-11z" fill="#fff"/>
        <circle cx="11" cy="11" r="4" fill="var(--lime)"/>
      </svg>
      42 Brindle Wold Hadley Cross, Wendshire KX27 4QD
    </div>
  </div>
</body>
</html>
```